Thank you for shopping with us business card

We would like a thank you card for our rebranded business. We used to be "Brindle Goods" but are now "Marlow Finds. Old thank you card and new logo will be attached for reference. New thank you card does not have to be same design as old thank you card, but please use new logo.
Shopmart URL is now marlowfinds.shopmart.example
Instagram is @Marlow_Finds
Email is marlowfinds@mailbox.example
Thank you!

Contact Information for Business Card

Shopmart site, email, Instagram

```html
<!DOCTYPE html>
<html lang="en">
<head>
<meta charset="utf-8">
<title>Marlow Finds – Business Card</title>
<link rel="stylesheet" href="https://fonts.googleapis.com/css2?family=Poppins:ital,wght@0,400;0,500;0,700;1,600&display=swap">
<style>
  :root {
    --backdrop: #d6d6d6;
    --card: #ffffff;
    --ink: #111111;
    --band-dark: #0a0a0a;
    --band-mid: #7a7a7a;
    --icon-hex: #bdbdbd;
    --icon-hex-light: #d9d9d9;
    --hairline: #e6e6e6;
    --on-band: #ffffff;
    --decor-soft: #ececec;
  }
  * { box-sizing: border-box; margin: 0; padding: 0; }
  html, body { width: 1200px; height: 1200px; overflow: hidden; }
  body {
    background: var(--backdrop);
    font-family: "Poppins", sans-serif;
    color: var(--ink);
    position: relative;
  }
  .card {
    position: absolute;
    left: 150px;
    width: 900px;
    height: 527px;
    background: var(--card);
    overflow: hidden;
  }
  .card--front { top: 56px; }
  .card--back { top: 616px; height: 528px; }

  /* Front */
  .front-accents { position: absolute; inset: 0; }
  .brand-block {
    position: absolute;
    left: 46px;
    top: 155px;
    width: 320px;
    text-align: center;
  }
  .brand-square {
    display: block;
    width: 124px;
    height: 124px;
    margin: 0 auto 68px;
    background: var(--ink);
  }
  .brand-name {
    font-weight: 700;
    font-size: 25px;
    line-height: 1.3;
    letter-spacing: 0.2px;
    text-transform: uppercase;
    white-space: nowrap;
  }
  .person {
    position: absolute;
    left: 444px;
    top: 134px;
  }
  .person__name {
    font-weight: 600;
    font-style: italic;
    font-size: 40px;
    line-height: 1.1;
  }
  .person__title {
    font-weight: 400;
    font-size: 21px;
    margin-top: 2px;
  }
  .contact-list {
    position: absolute;
    left: 428px;
    top: 279px;
    width: 472px;
    list-style: none;
  }
  .contact-band {
    height: 50px;
    margin-bottom: 3px;
    display: flex;
    align-items: center;
    padding-left: 18px;
    clip-path: polygon(14px 0, 100% 0, 100% 100%, 14px 100%, 0 50%);
    background: var(--band-dark);
    color: var(--on-band);
    font-size: 23.5px;
    font-weight: 400;
    white-space: nowrap;
  }
  .contact-band--mid { background: var(--band-mid); }
  .contact-band__icon { width: 30px; height: 30px; margin-right: 15px; flex: none; }

  /* Back */
  .back-decor {
    position: absolute;
    left: 0;
    top: 0;
    width: 900px;
    height: 280px;
    background: linear-gradient(180deg, var(--decor-soft) 0%, var(--card) 100%);
  }
  .lockup {
    position: absolute;
    left: 231px;
    top: 322px;
    display: flex;
    align-items: center;
    gap: 33px;
  }
  .lockup__square {
    width: 106px;
    height: 106px;
    background: var(--ink);
    flex: none;
  }
  .lockup__divider {
    width: 2px;
    height: 128px;
    background: var(--ink);
    flex: none;
  }
  .lockup__name {
    font-weight: 700;
    font-size: 43px;
    line-height: 1.25;
    text-transform: uppercase;
    letter-spacing: 0.3px;
  }
</style>
</head>
<body>

<section class="card card--front" aria-label="Business card front">
  <svg class="front-accents" width="900" height="527" viewBox="0 0 900 527" aria-hidden="true">
    <line x1="569" y1="2" x2="800" y2="62" stroke="var(--hairline)" stroke-width="6"/>
    <line x1="838" y1="100" x2="885" y2="269" stroke="var(--hairline)" stroke-width="6"/>
  </svg>

  <div class="brand-block">
    <span class="brand-square" aria-hidden="true"></span>
    <p class="brand-name">Marlow Finds</p>
  </div>

  <div class="person">
    <p class="person__name">Corin Vale</p>
    <p class="person__title">President/CEO</p>
  </div>

  <ul class="contact-list">
    <li class="contact-band">
      <svg class="contact-band__icon" viewBox="0 0 30 30" aria-hidden="true">
        <polygon points="8,2 22,2 29,15 22,28 8,28 1,15" fill="var(--icon-hex)"/>
      </svg>
      @Marlow_Finds
    </li>
    <li class="contact-band contact-band--mid">
      <svg class="contact-band__icon" viewBox="0 0 30 30" aria-hidden="true">
        <polygon points="8,2 22,2 29,15 22,28 8,28 1,15" fill="var(--icon-hex-light)"/>
        <rect x="9" y="10" width="12" height="9" fill="var(--band-mid)"/>
        <polyline points="9,10 15,15 21,10" fill="none" stroke="var(--icon-hex-light)" stroke-width="1.2"/>
      </svg>
      marlowfinds@mailbox.example
    </li>
    <li class="contact-band">
      <svg class="contact-band__icon" viewBox="0 0 30 30" aria-hidden="true">
        <polygon points="8,2 22,2 29,15 22,28 8,28 1,15" fill="var(--icon-hex)"/>
        <circle cx="15" cy="15" r="6.5" fill="none" stroke="var(--band-dark)" stroke-width="1.6"/>
        <line x1="8.5" y1="15" x2="21.5" y2="15" stroke="var(--band-dark)" stroke-width="1.2"/>
        <ellipse cx="15" cy="15" rx="2.8" ry="6.5" fill="none" stroke="var(--band-dark)" stroke-width="1.2"/>
      </svg>
      marlowfinds.shopmart.example
    </li>
  </ul>
</section>

<section class="card card--back" aria-label="Business card back">
  <div class="back-decor" role="img" aria-label="Decorative radiating line artwork"></div>

  <div class="lockup">
    <span class="lockup__square" aria-hidden="true"></span>
    <span class="lockup__divider" aria-hidden="true"></span>
    <p class="lockup__name">Marlow<br>Finds</p>
  </div>
</section>

</body>
</html>
```